GUARANTEED! - Creation of Linqora Promotional Images (requires Photoshops to modify cars)

Hi all,

We will require 5 different images to be created although once the first one is completed, the look and theme can literally be copied across to the others. These promotional images are to represent the service our website offers as well as the benefit’s the user can receive. (please ask for the website via private message if required) Our website is literally a comparison website related to vehicle modifications - so we make it quick and easy for users to find the best deal with local Window Tinters, ECU Remappers, Alloy Wheel Refurbs & More.

Aim of the image - This is purely to be posted on linqora to push viewers to our website / linqora page (there will be links in the description when it’s posted on linqora) so the image needs to tell the user what we do and urge them to visit the website.

Target market - our target market is mainly the car enthusiast (ages between 17 - 25) although we’re looking to keep this promotional image simple, professional and with the use of light neutral colours.

Image to be created - (our idea, please feel free to change) - see attachment of rough sketch created titled : ‘Rough Sketch Promotional Image

Main title across the top will read ‘FIND THE BEST DEAL WITH :’ - The words best deal should stand out more and be of a larger font / potentially different colour, maybe orange to keep in theme with the website. Then as shown in the sketch, we will have car number 1 which has been photoshopped as stated further down . Then we will have arrows pointing onto the car which will state the different modifications that has been completed on the car e.g - arrow will point to the rear window and will state the words :

WINDOW TINTERS
IN YOUR AREA

(regarding the text stated above, we feel it would be best if they were all placed the same distance away from the car to keep the professional look) - we also feel the service mentioned such as ‘WINDOW TINTERS’ should be a larger font than the ‘IN YOUR AREA’

Each car will have 4 arrows pointing on different parts of the car with text added as stated above (hopefully the rough sketch will make all these requirements that little bit clearer)

Then underneath the car image with the 4 arrows and text, we will have a Call to action button (which should keep the same kind of theme as that on the website homepage, (green blackground of block with white text) - The text in this button will read ‘CLICK BELOW!’ - we also had the idea of adding an arrow under the Call to action button to point the users to the description below the image. (Needs to be clear space around the CTA so it stands out - apart from potentially this arrow)

Then finally we’d like to have our logo (quite small) to the bottom left of the image with the words ‘PLEASE SHARE!’ to the bottom right of the image.

As you can see, the requirements we’re after are quite simple so the time will be mostly in the photoshopping of the 5 cars.

Please refer to the rough sketch but if you have any questions, please contact us here.

PHOTOSHOPS REQUIRED

The changes made to each car will be partly left up to you - however it’s vitally important that it stands out yet doesn’t look ‘silly’ and needs to look realistic - looking realistic is important.

Photoshop requirements

Car 1 - Green Valtessa

- Possibly change colour - please feel free to try other colours (need to look realistic)
- Change the colour of the rear window to a limo style black.
- Change the colour of the roof (can only see a slight bit of it) to black
- Change the colour of the wheels (the colour used here will depend on the change colour of the actual car, some options we like include yellow, green, orange and red

Car 2 - White Korvane LX5

- Change the colour of the rear window and rear side window to a limo style black
- Change the colour of the roof to black (not decided whether it should be black/matt black so test)
- Change the colour of the wheels to a red/ orange

Car 3 - Blue Brivo

- Possibly change colour - please feel free to try other colours - maybe a red but needs to look realistic
- Change the colour of the rear window visible to a limo style black
- Change the colour of the roof to black
- Change the colour of the wheels to black

Car 4 - Yellow Korvane LX5

- Please try changing the colour of this to a metallic grey/dark silver / gloss dark blue.
- Change the colour of the wheels to a yellow

Car 5 - Black Korvane LX5 (first of all we need to remove the background of this image)

Please state if this is too difficult to photoshop and we’ll go from there.

- Colour change to red please - ensure looks realistic
- Change the colour of the wheels to a black

If any of the changes we’ve requested don’t look realistic when you’ve created them - please let us know and feel free to try other colours … remember, needs to look professional and realistic.

Background - up to you although we feel something quite neutral would work well - please however try out whatever you think would look good.

************* IMPORTANT - PLEASE READ *******************

To save you time and to avoid wasted effort, we'd like you to create the promotional image using image 1 ONLY first of all - once we're satisfied with that 100%, we would then ask you to complete the other 4 images (which shouldn't take long once the first image is complete)

*************************************************************************

Just to add - we have purchased the rights for these images but if you feel you've some car images that would suit our requirements better than these, please send them across to us for our opinion.

We may add to this brief so keep an eye out - we will also offer additional work to the winning designer - if you have any questions at all, please ask away.

Thanks,

Derek,
Updates

Still not there with the design all - keep them coming.Thanks Added Saturday, October 1, 2016

Project Deadline Extended Reason: Not happy with the designs receivec and only received a few different designers whereas the project I purchased stated I would receive alot more..Not impressed so far.Regards.Derek Added Monday, October 3, 2016

Target Market(s)

Car enthusiast / youthful - but needs to have the professional clear look - most important.

Industry/Entity Type

Promotional

Font styles to use
Serif
Sans Serif

Requirements
Must have
• - Title of 'FIND THE BEST DEAL WITH : '
• - Car image for each
• - 4 Arrows coming off car for each image with the text stated
• - Call to action button - that stands out
• - Logo and words 'Please share!' / 'Please share me!'
Nice to have
• Potential other car images (would need commercial right so would have to be free for commercial use or a suitable price to pay for the rights) - this is only if you feel you have an image that would be better than those we currently have.
Should not have
• Needs to be kept clear - points to stand out are the opening title of 'FIND THE BEST DEAL WITH :', Car and the service such as 'WINDOW TINTERS'

```html
<!DOCTYPE html>
<html lang="en">
<head>
<meta charset="utf-8">
<title>Find the Best Deal – Promotional Image</title>
<link rel="stylesheet" href="https://fonts.googleapis.com/css2?family=Open+Sans:wght@300;400;700&display=swap">
<style>
  :root {
    --backdrop: #cbc9cc;
    --orange: #f7a81b;
    --orange-deep: #f7931e;
    --green: #22cd8c;
    --car-green: #1c9a25;
    --ink: #4a4a4a;
    --black: #111111;
    --white: #ffffff;
    --cta-top: #f8d51c;
    --cta-bottom: #f4a90c;
    --cta-text: #e5176b;
  }
  html, body {
    margin: 0;
    padding: 0;
    width: 1200px;
    height: 1200px;
    overflow: hidden;
    background: var(--backdrop);
    font-family: "Open Sans", Arial, sans-serif;
  }
  .stage {
    position: absolute;
    left: 202px;
    top: 239px;
    width: 882px;
    height: 741px;
    transform: scale(0.9231);
    transform-origin: top left;
  }
  .promo {
    position: relative;
    width: 882px;
    height: 741px;
    background: var(--white);
    overflow: hidden;
  }
  .promo-shapes {
    position: absolute;
    inset: 0;
  }
  .headline {
    position: absolute;
    left: 0;
    right: 0;
    top: 62px;
    margin: 0;
    text-align: center;
    font-weight: 700;
    color: var(--ink);
    font-size: 40px;
    line-height: 1;
    white-space: nowrap;
    padding-left: 12px;
  }
  .headline .highlight {
    color: var(--orange);
    font-size: 70px;
    vertical-align: -2px;
    margin: 0 6px;
  }
  .service {
    position: absolute;
    text-align: center;
    transform: translateX(-50%);
    font-size: 18px;
    line-height: 18px;
    white-space: nowrap;
  }
  .service-name {
    display: block;
    color: var(--orange-deep);
    font-weight: 300;
  }
  .service-area {
    display: block;
    color: var(--black);
    font-weight: 400;
  }
  .service--tint { left: 243px; top: 215px; }
  .service--roof { left: 539px; top: 233px; }
  .service--ecu  { left: 754px; top: 331px; }
  .service--alloy { left: 143px; top: 375px; }
  .car-photo {
    position: absolute;
    left: 228px;
    top: 348px;
    width: 573px;
    height: 253px;
    border-radius: 46% 54% 14% 18% / 58% 52% 30% 30%;
    background: linear-gradient(160deg, #2aa332 0%, var(--car-green) 55%, #0f5e15 100%);
  }
  .cta {
    position: absolute;
    left: 310px;
    top: 617px;
    width: 250px;
    height: 62px;
    border-radius: 12px;
    background: linear-gradient(180deg, var(--cta-top) 0%, var(--cta-bottom) 100%);
    color: var(--cta-text);
    font-size: 24px;
    font-weight: 300;
    display: flex;
    align-items: center;
    justify-content: center;
  }
  .brand {
    position: absolute;
    left: 44px;
    top: 685px;
    font-size: 17px;
    font-weight: 700;
    letter-spacing: 3px;
    color: var(--ink);
  }
  .share {
    position: absolute;
    right: 40px;
    top: 686px;
    font-size: 22px;
    font-weight: 700;
    color: var(--ink);
  }
</style>
</head>
<body>
  <div class="stage">
    <section class="promo">
      <svg class="promo-shapes" width="882" height="741" viewBox="0 0 882 741" aria-hidden="true">
        <path class="top-band" d="M0,0 H882 V125 Q441,-39 0,125 Z" fill="var(--orange)"/>
        <path class="accent-band" d="M0,424 Q420,602 882,497 L882,505 Q420,640 0,442 Z" fill="var(--orange-deep)"/>
        <path class="ground" d="M0,442 Q420,640 882,505 L882,741 L0,741 Z" fill="var(--green)"/>
        <path class="ground-edge" d="M0,423 Q420,600 882,496" fill="none" stroke="var(--black)" stroke-width="3"/>
        <g class="leaders" fill="none" stroke-width="1.2" stroke-dasharray="3 3">
          <polyline points="237,259 258,327 322,362" stroke="#1a8a5a"/>
          <line x1="530" y1="276" x2="460" y2="345" stroke="#1a8a5a"/>
          <line x1="757" y1="375" x2="752" y2="490" stroke="var(--orange-deep)"/>
          <line x1="145" y1="418" x2="228" y2="505" stroke="#e5176b"/>
        </g>
      </svg>

      <h1 class="headline">FIND THE<span class="highlight">BEST DEAL</span>WITH :</h1>

      <div class="car-photo" role="img" aria-label="Photo of a green sports hatchback with tinted windows, black roof and dark alloy wheels"></div>

      <p class="service service--tint"><span class="service-name">WINDOWS TINTER</span><span class="service-area">IN YOUR AREA</span></p>
      <p class="service service--roof"><span class="service-name">ROOF VINYL WRAPPERS</span><span class="service-area">IN YOUR AREA</span></p>
      <p class="service service--ecu"><span class="service-name">ECU REMAPPERS</span><span class="service-area">IN YOUR AREA</span></p>
      <p class="service service--alloy"><span class="service-name">ALLOY WHEELS REFURBERS</span><span class="service-area">IN YOUR AREA</span></p>

      <div class="cta">CLICK BELLOW!</div>

      <div class="brand">TUNEWISE</div>
      <div class="share">PLEASE SHARE</div>
    </section>
  </div>
</body>
</html>
```